Website design for Meridian Tote printing specialist

We need an overhaul of our website front end design. We need a new look and a modern take on the products we sell and service we offer. We sell plain stock in a variety of bag types and offer a printing service of customers branding and logos. Customers request online quotes and this facility must be an easy one step process for users. Our logo is currently green and orange and we are not really looking for re branding at this stage. The final design must communicate that we are the leading printing specialist throughout the country, have been in operation for 15 years and have a vast amount of experience and expertise. The design must instantly show the products available and the ability to request a quote for the desired product.

Target Market(s)

Trade shows, retailers, dentists, food suppliers. wine makers etc etc and anyone that uses carry bags

Industry/Entity Type

Screen Printing

Number of Pages Required

5+ page

Font styles to use
Serif
Sans Serif

Colors

Designer to choose colors to be used in the design.

Requirements
Must have
• Our home page featuring all the products as selectable entities and a short description of what each bag type is when the user hovers over the image.
• Then the product landing pages must show different sizes of that product type. On each page there must be a quick quote button that goes to the quote screen with the features and information to select or include for a quote to be processed. The logo is green and orange and still should have this present but happy to move away from this on the website pages in general.I have so many product pictures and unable to upload them all here. The categories for products are as follows:
• Kraft Paper Bags
• Laminated bags
• Non-woven bags
• Calico bags
• Wine bags
• Florist bags
• Plastic Bags
• Printed Bags
• Gift Boxes
• Tissue paper
• Wrapping Paper
• Custom Bags and Boxes
• There also needs to be a gallery page that showcases work we have done. The ability to have a description for each photo in the gallery would be great.
• A general bag size page would be great and one content page that is about us and another for contact us.
• A free sample button so a user can request a sample. Phone number must be included on this page and unable to submit with a valid phone number.
• Our phone number should be prominent.
• A search feature please.
Nice to have
• Fonts should be in keeping with the design of the website
Should not have
• I dont want users having to scroll too far down to find information. The icons of the bags on the home screen should almost appear on one screen.
• I can upload all my content and pictures so no need to get them from me. I really want your look and feel and design layout that i can then work from.

```html
<!DOCTYPE html>
<html lang="en">
<head>
<meta charset="utf-8">
<title>Meridian Tote – Wholesale Printed Bags and Boxes</title>
<link rel="stylesheet" href="https://fonts.googleapis.com/css2?family=Audiowide&family=Poppins:wght@400;500;600;700&display=swap">
<style>
:root{
  --green:#3f9a1f;
  --green-dark:#1f6a1a;
  --orange:#f07d1a;
  --blue:#3d4fb8;
  --teal:#6fcad2;
  --teal-footer:#8fd3dc;
  --ink:#2b2b2b;
  --muted:#777;
  --card:#f3f4f8;
  --line:#e3e5ea;
  --white:#fff;
}
*{box-sizing:border-box;margin:0;padding:0}
html,body{width:1200px;height:3429px;overflow:hidden}
body{position:relative;background:var(--white);font-family:"Poppins",sans-serif;color:var(--ink)}
.abs{position:absolute}
.heading{font-family:"Audiowide",sans-serif;color:var(--green);font-weight:400;font-size:27px;text-align:center;width:1200px;left:0}
.btn{display:flex;align-items:center;justify-content:center;color:var(--white);font-size:10px;font-weight:600;letter-spacing:.5px;text-transform:uppercase}
.btn-blue{background:var(--blue)}
.btn-orange{background:var(--orange)}
.logo{display:flex;align-items:center;gap:10px;font-weight:700;font-size:30px;color:var(--green-dark);line-height:1}
.logo .dot{width:22px;height:22px;border-radius:50%;background:var(--orange);flex:none}

/* header */
.header{left:0;top:0;width:1200px;height:119px;background:var(--white)}
.call-top{left:597px;top:28px;font-size:13px;color:var(--green);display:flex;gap:10px;align-items:center}
.nav a{position:absolute;white-space:nowrap;color:var(--ink);text-decoration:none;font-size:12.5px;font-weight:500}
.nav a.active{color:var(--green)}

/* hero */
.hero{left:0;top:119px;width:1200px;height:521px;background:var(--teal);overflow:hidden}
.hero-photo{left:560px;top:0;width:640px;height:521px;
  background:
    linear-gradient(90deg,var(--teal) 0%,rgba(111,202,210,0) 22%,rgba(111,202,210,0) 82%,var(--teal) 100%),
    linear-gradient(180deg,#f1e6dc 0%,#e4cdbd 30%,#c9b4a6 55%,#a9a29c 75%,#d9dfe2 100%)}
.hero-title{left:87px;top:120px;font-size:29px;line-height:1.45;color:var(--white);font-weight:500}
.hero-title span{font-family:"Audiowide",sans-serif;font-weight:400}
.hero-dots{left:87px;display:flex;gap:6px}
.hero-dots i{width:14px;height:14px;border:2px solid #2b4a55;border-radius:50%;display:block}
.hero-dots i:first-child{background:#2b4a55}

/* products */
.grid{left:87px;top:777px;width:1026px;display:grid;grid-template-columns:repeat(6,162px);column-gap:10.8px;row-gap:12px}
.card{height:272px;background:var(--white);border:1px solid var(--line);display:flex;flex-direction:column}
.card .shot{height:204px;background:var(--card)}
.card .name{flex:1;display:flex;align-items:center;justify-content:center;text-align:center;font-size:12.5px;font-weight:600;line-height:1.25;padding:0 10px}
.card.active .name{color:var(--green)}

/* gallery */
.tile{position:absolute}
.tile-cap{position:absolute;left:0;right:0;top:95px;text-align:center;color:var(--white);font-weight:600;font-size:18px}

/* testimonial */
.reviews{left:0;top:2176px;width:1200px;height:448px;background:#f5f6fa}
.quote{left:313px;top:2377px;width:574px;text-align:center;font-size:11.5px;line-height:1.65;color:#555}
.client{left:0;width:1200px;text-align:center}
.rev-dots{left:1024px;top:2362px;display:flex;flex-direction:column;gap:6px}
.rev-dots i{width:14px;height:14px;border:1.5px solid #555;border-radius:50%;display:block}
.rev-dots i.on{background:radial-gradient(#555 35%,transparent 40%)}

/* features */
.feature{top:2720px;width:340px;text-align:center}
.feature .ico{width:80px;height:80px;margin:0 auto;border-radius:50%;border:1px solid var(--line);display:flex;align-items:center;justify-content:center}
.feature h3{margin-top:22px;font-size:14px;font-weight:600}
.feature p{margin-top:8px;font-size:11.5px;color:var(--muted);line-height:1.4}
.divider{top:2730px;width:1px;height:140px;background:var(--line)}

/* footer */
.footer{left:0;top:2963px;width:1200px;height:466px;background:var(--teal-footer)}
.foot-head{font-family:"Audiowide",sans-serif;color:var(--white);font-size:15px}
.foot-list{list-style:none;font-size:11.5px;color:#2b3a44}
.foot-list li{height:28.5px}
.field{border:1px solid rgba(255,255,255,.8);color:var(--white);font-size:10px;padding:0 10px;display:flex;align-items:center}
.social{top:3259px;width:28px;height:28px;border:1.5px solid var(--orange);display:flex;align-items:center;justify-content:center}
.social i{width:10px;height:10px;background:var(--orange);display:block;border-radius:2px}
.social.on{background:var(--orange)}
.social.on i{background:var(--white)}
.legal{left:87px;top:3350px;font-size:10.5px;color:#2b3a44}
.legal b{color:var(--orange);font-weight:500}
</style>
</head>
<body>

<header class="abs header">
  <div class="abs logo" style="left:87px;top:44px"><span class="dot"></span>Meridian Tote</div>
  <div class="abs call-top">Call Us
    <svg width="14" height="14" viewBox="0 0 24 24"><path fill="#3f9a1f" d="M6.6 10.8a15 15 0 006.6 6.6l2.2-2.2a1 1 0 011-.25 11.4 11.4 0 003.6.57 1 1 0 011 1V20a1 1 0 01-1 1A17 17 0 013 4a1 1 0 011-1h3.5a1 1 0 011 1c0 1.25.2 2.45.57 3.57a1 1 0 01-.25 1z"/></svg>
    1300 - 482 - 915</div>
  <div class="abs btn btn-blue" style="left:839px;top:20px;width:128px;height:33px">Get a Sample</div>
  <div class="abs btn btn-orange" style="left:983px;top:20px;width:128px;height:33px">Get a Quote</div>
  <nav class="abs nav" style="left:0;top:78px">
    <a class="active" style="left:400px">Home</a>
    <a style="left:483px">About Us</a>
    <a style="left:588px">Products ⌄</a>
    <a style="left:711px">Gallery</a>
    <a style="left:804px">Review</a>
    <a style="left:897px">Contact Us</a>
  </nav>
  <svg class="abs" style="left:1035px;top:74px" width="26" height="22" viewBox="0 0 26 22"><path d="M1 2h4l3 12h12l3-9H7" fill="none" stroke="#555" stroke-width="1.8"/><circle cx="10" cy="18" r="1.8" fill="#555"/><circle cx="19" cy="18" r="1.8" fill="#555"/><circle cx="22" cy="4" r="4" fill="#f07d1a"/></svg>
  <svg class="abs" style="left:1090px;top:76px" width="18" height="18" viewBox="0 0 18 18"><circle cx="7.5" cy="7.5" r="6" fill="none" stroke="#555" stroke-width="1.8"/><path d="M12 12l5 5" stroke="#555" stroke-width="1.8"/></svg>
</header>

<section class="abs hero">
  <div class="abs hero-photo" role="img" aria-label="Customer in a sun hat holding printed shopping bags"></div>
  <h1 class="abs hero-title">We are a wholesale<br>supplier of <span>Printed Bags</span><br>and <span>Boxes</span></h1>
  <div class="abs btn btn-orange" style="left:87px;top:295px;width:130px;height:32px">Get a Sample</div>
  <div class="abs hero-dots" style="top:428px"><i></i><i></i><i></i><i></i></div>
</section>

<h2 class="abs heading" style="top:712px">Featured Products</h2>
<div class="abs grid">
  <div class="card"><div class="shot" role="img" aria-label="Kraft paper bag" style="background:radial-gradient(ellipse 45% 50% at 50% 55%,#b08a5f 0%,#d9c3a8 55%,var(--card) 100%)"></div><div class="name">Kraft Paper<br>Bags</div></div>
  <div class="card"><div class="shot" role="img" aria-label="Black laminated bag" style="background:radial-gradient(ellipse 45% 45% at 50% 55%,#2a2a2a 0%,#8d8e93 55%,var(--card) 100%)"></div><div class="name">Laminated<br>Bags</div></div>
  <div class="card active"><div class="shot" role="img" aria-label="Natural non-woven tote" style="background:radial-gradient(ellipse 45% 50% at 50% 55%,#e8d9c4 0%,#f3ece2 55%,#fff 100%)"></div><div class="name">Non-Woven<br>Bags</div></div>
  <div class="card"><div class="shot" role="img" aria-label="Blue calico bag" style="background:radial-gradient(ellipse 45% 40% at 50% 55%,#1e9fd8 0%,#93cfe9 55%,var(--card) 100%)"></div><div class="name">Calico Bags</div></div>
  <div class="card"><div class="shot" role="img" aria-label="Wine bottle bag" style="background:radial-gradient(ellipse 22% 50% at 50% 50%,#5a3d24 0%,#b7a592 60%,var(--card) 100%)"></div><div class="name">Wine Bags</div></div>
  <div class="card"><div class="shot" role="img" aria-label="Jute florist bag" style="background:radial-gradient(ellipse 45% 45% at 50% 55%,#5c9a48 0%,#c9c08f 55%,var(--card) 100%)"></div><div class="name">Florist Bags</div></div>
  <div class="card"><div class="shot" role="img" aria-label="Pink plastic bag" style="background:radial-gradient(ellipse 45% 38% at 50% 55%,#e8337f 0%,#f2a3c4 55%,var(--card) 100%)"></div><div class="name">Plastic Bags</div></div>
  <div class="card"><div class="shot" role="img" aria-label="Printed paper bag" style="background:radial-gradient(ellipse 40% 48% at 50% 55%,#2f5a3a 0%,#b89a76 55%,var(--card) 100%)"></div><div class="name">Printed Bags</div></div>
  <div class="card"><div class="shot" role="img" aria-label="Grey gift box" style="background:radial-gradient(ellipse 42% 35% at 50% 55%,#aeb1a4 0%,#d3d5cd 55%,var(--card) 100%)"></div><div class="name">Gift Boxes</div></div>
  <div class="card"><div class="shot" role="img" aria-label="Turquoise tissue paper pack" style="background:radial-gradient(ellipse 45% 22% at 50% 52%,#2dbdc6 0%,#a2e0e4 55%,var(--card) 100%)"></div><div class="name">Tissue Paper</div></div>
  <div class="card"><div class="shot" role="img" aria-label="Pink wrapping pack" style="background:radial-gradient(ellipse 42% 28% at 50% 55%,#e46b76 0%,#f1b4b9 55%,var(--card) 100%)"></div><div class="name">Wrapping<br>Paper</div></div>
  <div class="card"><div class="shot" role="img" aria-label="Kraft custom box" style="background:radial-gradient(ellipse 40% 36% at 50% 55%,#8e623e 0%,#c9aa8c 55%,var(--card) 100%)"></div><div class="name">Custom Bags &amp;<br>Boxes</div></div>
</div>
<div class="abs btn btn-blue" style="left:519px;top:1367px;width:160px;height:30px">See our Products</div>

<h2 class="abs heading" style="top:1470px">Our Work Gallery</h2>
<div class="tile" role="img" aria-label="Kitchen shelf with a printed wine bag" style="left:87px;top:1536px;width:644px;height:238px;background:linear-gradient(180deg,#f1efeb 0%,#e4ded6 45%,#b9ab98 75%,#8c7b66 100%)"></div>
<div class="tile" role="img" aria-label="Black and white non-woven bags on orange" style="left:736px;top:1536px;width:377px;height:238px;background:radial-gradient(ellipse 60% 55% at 50% 50%,#f3b25e 0%,#eb9a3a 60%,#e48c2c 100%)"></div>
<div class="tile" role="img" aria-label="Person carrying a printed canvas tote" style="left:87px;top:1783px;width:338px;height:240px;background:linear-gradient(180deg,#eeece8 0%,#ddd4c5 50%,#c4b196 80%,#8d7a62 100%)"></div>
<div class="tile" role="img" aria-label="Printed kraft and white paper bags" style="left:434px;top:1783px;width:332px;height:240px;background:linear-gradient(180deg,#6f6d69 0%,#8e8a84 50%,#a9a39a 100%)">
  <div class="tile-cap">Kraft Paper Bags</div>
</div>
<div class="tile" role="img" aria-label="Assorted printed bags and pouches" style="left:775px;top:1783px;width:338px;height:240px;background:linear-gradient(180deg,#d2f1f3 0%,#c5e7ea 40%,#b9c5bd 70%,#a89684 100%)"></div>
<div class="abs btn btn-blue" style="left:519px;top:2064px;width:160px;height:30px">See our Gallery</div>

<section class="abs reviews"></section>
<h2 class="abs heading" style="top:2248px">What Our Clients Say</h2>
<svg class="abs" style="left:580px;top:2312px" width="40" height="30" viewBox="0 0 40 30"><path d="M2 28V16C2 8 6 3 14 1l2 4c-5 2-7 5-7 9h7v14zm22 0V16c0-8 4-13 12-15l2 4c-5 2-7 5-7 9h7v14z" fill="#f07d1a"/></svg>
<p class="abs quote">Westbrook Valley Council have used Meridian Tote to produce quality paper showbags for our Careers and Jobs Expo for two years. The bags were produced both within timelines and budget. We were very satisfied with the bags, and more importantly given the objective of the Expo, we were able to use a local supplier.</p>
<div class="abs client" style="top:2457px;font-size:13px;font-weight:600">Lena Hartwell</div>
<div class="abs client" style="top:2478px;font-size:10px;color:var(--muted)">Business Support Officer</div>
<div class="abs btn btn-blue" style="left:505px;top:2526px;width:190px;height:32px">Read a few Testimonials</div>
<div class="abs rev-dots"><i></i><i class="on"></i><i></i><i></i></div>

<div class="abs feature" style="left:77px">
  <div class="ico"><svg width="34" height="26" viewBox="0 0 34 26"><path d="M2 4h18v14H2zM20 9h7l5 5v4H20z" fill="none" stroke="#f07d1a" stroke-width="2"/><circle cx="8" cy="21" r="3" fill="#fff" stroke="#f07d1a" stroke-width="2"/><circle cx="26" cy="21" r="3" fill="#fff" stroke="#f07d1a" stroke-width="2"/></svg></div>
  <h3>Fast Turnaround</h3>
  <p>There are many variations of passages<br>of Lorem Ipsum available.</p>
</div>
<div class="abs divider" style="left:425px"></div>
<div class="abs feature" style="left:431px">
  <div class="ico"><svg width="20" height="34" viewBox="0 0 20 34"><text x="10" y="28" text-anchor="middle" font-family="Poppins,sans-serif" font-size="30" fill="#3f9a1f">$</text></svg></div>
  <h3>Best Prices</h3>
  <p>There are many variations of passages<br>of Lorem Ipsum available.</p>
</div>
<div class="abs divider" style="left:777px"></div>
<div class="abs feature" style="left:781px">
  <div class="ico"><svg width="32" height="28" viewBox="0 0 32 28"><path d="M1 3h5l4 15h15l4-11H8" fill="none" stroke="#3d4fb8" stroke-width="2.2"/><circle cx="12" cy="23" r="2.4" fill="#3d4fb8"/><circle cx="23" cy="23" r="2.4" fill="#3d4fb8"/></svg></div>
  <h3>Wide Range</h3>
  <p>There are many variations of passages<br>of Lorem Ipsum available.</p>
</div>

<footer class="abs footer"></footer>
<div class="abs logo" style="left:87px;top:3026px"><span class="dot"></span>Meridian Tote</div>
<div class="abs" style="left:87px;top:3120px;font-size:13px;color:var(--white)">Call Us: 1300 - 482 - 915</div>
<div class="abs" style="left:87px;top:3142px;font-size:12px;color:#2b3a44">hello@meridiantote.com</div>
<div class="abs" style="left:87px;top:3186px;font-size:10px;font-weight:600;color:#2b3a44">ADDRESS:</div>
<div class="abs" style="left:87px;top:3204px;font-size:11.5px;color:#2b3a44">PO Box 218, Larkfield Vic. 3521</div>
<div class="abs social" style="left:89px"><i></i></div>
<div class="abs social on" style="left:128px"><i></i></div>
<div class="abs social" style="left:167px"><i></i></div>
<div class="abs social" style="left:206px"><i></i></div>

<div class="abs foot-head" style="left:375px;top:3042px">Bags &amp; Boxes</div>
<ul class="abs foot-list" style="left:375px;top:3093px">
  <li>Kraft Paper Bags</li><li>Laminated bags</li><li style="text-decoration:underline">Non-woven bags</li><li>Calico bags</li><li>Wine Bags</li><li>Florist Bags</li><li>Plastic Bags</li>
</ul>
<ul class="abs foot-list" style="left:533px;top:3093px">
  <li>Printed Bags</li><li>Gift Boxes</li><li>Tissue Paper</li><li>Wrapping Paper</li><li>Custom Bags and Boxes</li>
</ul>

<div class="abs foot-head" style="left:734px;top:3042px">Get a Quote</div>
<div class="abs field" style="left:731px;top:3097px;width:183px;height:30px">Name</div>
<div class="abs field" style="left:928px;top:3097px;width:183px;height:30px">Phone</div>
<div class="abs field" style="left:731px;top:3141px;width:380px;height:30px">Email</div>
<div class="abs field" style="left:731px;top:3184px;width:380px;height:60px;align-items:flex-start;padding-top:8px">Message</div>
<div class="abs btn btn-orange" style="left:731px;top:3260px;width:81px;height:30px">Send ›</div>

<div class="abs legal">© 2019 <b>Meridian Tote</b>. All Right Reserved. &nbsp; <u>Terms &amp; Conditions</u> &nbsp; | &nbsp; Privacy Policy</div>
<svg class="abs" style="left:1094px;top:3346px" width="16" height="16" viewBox="0 0 16 16"><path d="M8 2L2 14h12z" fill="none" stroke="#f07d1a" stroke-width="1.8"/></svg>

</body>
</html>
```